Orvane Constructions Business card and Logo

We are a building company that would like our current logo design copied with the "Orvane Constructions" lines thicker.
We would also like our business cards copied with some minor copy changes. I have attached images of our logo and business cards.
We would like a standard size business card in landscape format rather than portrait.
On the back of the business card we would like a name added above the mobile number - "Remy Castellan"
Can I please get high res file of the logo and business cards at completion of redesign?

```html
<!DOCTYPE html>
<html lang="en">
<head>
<meta charset="utf-8">
<title>Orvane Constructions – Business Card</title>
<link rel="stylesheet" href="https://fonts.googleapis.com/css2?family=Ubuntu:wght@400;500;700&display=swap">
<style>
  :root {
    --stage: #e9eaea;
    --brand-green: #2e9e34;
    --brand-green-dark: #26872b;
    --pattern-green: #cfe6d3;
    --card-white: #ffffff;
    --ink: #1d1d1d;
    --ink-soft: #5a5a5a;
    --shadow: rgba(0, 0, 0, 0.18);
  }
  * { box-sizing: border-box; margin: 0; padding: 0; }
  html, body {
    width: 1200px;
    height: 783px;
    overflow: hidden;
    background: var(--stage);
    font-family: "Ubuntu", sans-serif;
  }
  .stage {
    position: relative;
    width: 1200px;
    height: 783px;
    display: flex;
    align-items: center;
    justify-content: center;
    gap: 40px;
  }
  .card {
    position: relative;
    width: 540px;
    height: 330px;
    border-radius: 4px;
    overflow: hidden;
    box-shadow: 0 6px 18px var(--shadow);
  }

  /* Back of card */
  .card--back { background: var(--brand-green); }
  .card--back .card__pattern {
    position: absolute;
    inset: 0;
    background: linear-gradient(160deg, rgba(255,255,255,0.10), rgba(255,255,255,0) 55%, rgba(255,255,255,0.08));
  }
  .card--back .wordmark {
    position: absolute;
    inset: 0;
    display: flex;
    align-items: center;
    justify-content: center;
    gap: 14px;
    color: var(--card-white);
    font-weight: 700;
    font-size: 44px;
    letter-spacing: 0.5px;
  }
  .wordmark__dot {
    width: 16px;
    height: 16px;
    border-radius: 50%;
    background: currentColor;
    flex: none;
  }

  /* Front of card */
  .card--front { background: var(--card-white); }
  .card--front .card__pattern {
    position: absolute;
    inset: 0;
    background: linear-gradient(100deg, var(--card-white) 0%, #f1f8f2 35%, #e6f2e8 70%, #f4faf5 100%);
  }
  .card--front .wordmark {
    position: absolute;
    left: 28px;
    top: 30px;
    display: flex;
    align-items: center;
    gap: 8px;
    color: var(--brand-green);
    font-weight: 700;
    font-size: 19px;
  }
  .card--front .wordmark__dot { width: 9px; height: 9px; }
  .registration {
    position: absolute;
    right: 26px;
    top: 36px;
    text-align: left;
    color: var(--ink-soft);
    font-size: 14px;
    line-height: 1.35;
    letter-spacing: 0.3px;
  }
  .contact {
    position: absolute;
    left: 0;
    right: 0;
    top: 112px;
    text-align: center;
    color: var(--ink);
    font-size: 17px;
    line-height: 1.3;
  }
  .contact__name { font-weight: 500; font-size: 18px; }
  .address {
    position: absolute;
    left: 0;
    right: 0;
    bottom: 26px;
    text-align: center;
    color: var(--ink);
    font-size: 18px;
    letter-spacing: 0.2px;
  }
</style>
</head>
<body>
  <main class="stage">
    <section class="card card--back" aria-label="Business card back">
      <div class="card__pattern" role="img" aria-label="Faint line pattern of building shapes on green"></div>
      <div class="wordmark">
        <span class="wordmark__name">Orvane Constructions</span>
        <span class="wordmark__dot"></span>
      </div>
    </section>

    <section class="card card--front" aria-label="Business card front">
      <div class="card__pattern" role="img" aria-label="Faint pale green line pattern of building shapes"></div>
      <div class="wordmark">
        <span class="wordmark__name">Orvane Constructions</span>
        <span class="wordmark__dot"></span>
      </div>
      <p class="registration">ACN-300 418 926<br>ABN-51300 418 926</p>
      <div class="contact">
        <p class="contact__name">Remy Castellan</p>
        <p>Ph-0400 512 386</p>
        <p>Web-orvane.example.au</p>
        <p>Email-remy@orvane.example.au</p>
        <p>Fax-03 9555 2740</p>
      </div>
      <p class="address">PO Box 417 Fernvale, Vic 3999</p>
    </section>
  </main>
</body>
</html>
```